Redesign existing website to have updated look and content

have existing website but do not have the time to put page detail that I want into it. we are a residential, family owned and operated HVAC and plumbing company. we offer service, repair, replacement, maintenance, new installations. the owner has over 20 years experience. got into his own business bc of high pricing charged by old employer. we believe CUSTOMER SERVICE IS THE ONLY THING THAT MATTERS, we are an harlow's guide top trade award winner. we just recently were invited to sell on Brindlemart. we currently have the owner and 1 other tech and a helper in the field. we want to keep small so that service doesn't suffer

Target Market(s)

homeowners over 28 in the Bucks and Montgomery and Delawre Counties of PA

Industry/Entity Type

Hvac

Number of Pages Required

4 page

Font styles to use
Serif
Sans Serif
Decorative

Colors
0255a3
ec1f27

Requirements
Must have
• more content and information
• online scheduling thru V Cita
• information that is not related to HVAC that can be updated daily
Nice to have
• apps that customers will be drawn to website with
• information regarding our services and costs
• online scheduling
• better content!!!!
• links to vendors and outside information

```html
<!DOCTYPE html>
<html lang="en">
<head>
<meta charset="utf-8">
<title>Halvern Service — Heating, Cooling &amp; Plumbing</title>
<link rel="stylesheet" href="https://fonts.googleapis.com/css2?family=Open+Sans:wght@400;600;700&display=swap">
<style>
:root{
  --blue:#0255a3;
  --red:#ec1f27;
  --ink:#2f3438;
  --muted:#7a7f84;
  --line:#e3e5e8;
  --panel:#2b3036;
  --footer:#3a3f45;
  --footer-text:#b9bec3;
  --soft:#eef0f2;
}
*{box-sizing:border-box;margin:0;padding:0}
html,body{width:1200px;height:2168px;overflow:hidden}
body{font-family:"Open Sans",Arial,sans-serif;color:var(--ink);background:#fff;position:relative}
.topline{height:6px;background:var(--red)}
.header{position:relative;height:106px;border-bottom:1px solid var(--line)}
.contact-strip{position:absolute;left:96px;top:6px;display:flex;gap:26px;font-size:11px;color:var(--muted)}
.contact-strip span{display:flex;align-items:center;gap:6px}
.brand{position:absolute;left:96px;top:34px;display:flex;align-items:center;gap:12px}
.brand-dot{width:40px;height:40px;border-radius:50%;background:var(--red)}
.brand-name{font-size:24px;font-weight:700;color:var(--blue);line-height:1.05;text-transform:uppercase;letter-spacing:.5px}
.nav{position:absolute;right:96px;top:56px;display:flex;gap:6px}
.nav a{font-size:11px;font-weight:600;color:var(--ink);text-decoration:none;padding:8px 14px;text-transform:uppercase}
.nav a.active{color:var(--blue);border:1px solid var(--blue)}
.hero{position:relative;height:388px}
.hero-photo{position:absolute;inset:0;background:linear-gradient(160deg,#b9c3cc 0%,#8e9aa5 40%,#5f6a74 75%,#7d8790 100%)}
.booking{position:absolute;left:700px;top:16px;width:460px;height:356px;background:rgba(43,48,54,.92);padding:22px 34px}
.booking h2{color:#fff;font-size:26px;font-weight:600;text-align:center;margin-bottom:22px}
.field-row{display:flex;gap:10px;margin-bottom:10px}
.field{flex:1;height:28px;background:#fff;font-size:10px;color:#9aa0a6;padding:7px 8px}
.field.tall{height:28px}
.note{font-size:9px;color:#c9cdd1;margin:4px 0 14px}
.submit{display:block;margin:0 auto;width:170px;height:38px;background:var(--blue);color:#fff;font-weight:700;font-size:15px;text-align:center;line-height:38px;border-bottom:3px solid #013c74;text-transform:uppercase}
.offer{padding-top:70px}
.section-title{text-align:center;font-size:26px;font-weight:600;color:var(--ink)}
.offer-grid{margin:40px auto 0;width:912px;display:grid;grid-template-columns:repeat(3,288px);gap:28px 24px}
.tile{position:relative;height:252px;overflow:hidden}
.tile.short{height:192px}
.tile-photo{position:absolute;inset:0}
.tile-label{position:absolute;left:0;right:0;bottom:0;height:40px;background:rgba(30,34,38,.72);color:#fff;font-size:12px;font-weight:600;text-transform:uppercase;text-align:center;line-height:40px}
.p1{background:linear-gradient(135deg,#c8c4bd,#8d8a84)}
.p2{background:linear-gradient(135deg,#a9b3bd,#e6e9ec)}
.p3{background:linear-gradient(135deg,#b7bec6,#5f6f84)}
.p4{background:linear-gradient(135deg,#cfc8c0,#8a7d6f)}
.p5{background:linear-gradient(135deg,#5c6670,#a3abb3)}
.p6{background:linear-gradient(135deg,#8f9aa3,#c9d0d5)}
.more-btn{display:block;margin:36px auto 0;width:250px;height:36px;background:var(--blue);color:#fff;font-size:11px;font-weight:600;text-align:center;line-height:36px;border-radius:3px;text-transform:uppercase}
.about-row{margin:76px auto 0;width:912px;display:flex;gap:40px}
.about{width:436px}
.about h3,.newsletter h3{font-size:22px;font-weight:600;margin-bottom:18px}
.about-body{display:flex;gap:16px}
.about-photo{width:216px;height:150px;background:linear-gradient(135deg,#e7c25a,#7a8fa4)}
.about-text{flex:1;font-size:11px;line-height:1.55;color:var(--muted)}
.about-text a{color:var(--blue);font-weight:700;text-decoration:none}
.newsletter{width:436px;height:216px;background:var(--soft);padding:26px 28px}
.newsletter p{font-size:11px;color:var(--muted);line-height:1.5;margin-bottom:18px}
.sub-row{display:flex;gap:10px}
.sub-field{width:240px;height:28px;background:#fff;border:1px solid var(--line);font-size:10px;color:#9aa0a6;padding:7px 8px}
.sub-btn{width:96px;height:28px;background:var(--blue);color:#fff;font-size:10px;font-weight:600;text-align:center;line-height:28px}
.award{position:absolute;left:0;top:1552px;width:1200px;height:176px;background:var(--red)}
.award-text{position:absolute;left:144px;top:36px;width:640px;color:#fff}
.award-text h2{font-size:34px;font-weight:600;line-height:1.15;margin-bottom:12px}
.award-text p{font-size:13px;opacity:.9;line-height:1.5}
.award-badge{position:absolute;left:864px;top:36px;width:104px;height:104px;border-radius:50%;background:#fff;display:flex;align-items:center;justify-content:center}
.award-badge span{width:68px;height:68px;border-radius:50%;background:#3f8f3a;border:4px solid #e0b53a}
.partners{position:absolute;left:0;top:1728px;width:1200px;height:232px;border-top:1px solid var(--line)}
.partner-row{position:absolute;left:144px;width:912px;display:flex;justify-content:space-between}
.partner-row.r1{top:78px}
.partner-row.r2{top:138px}
.partner{font-size:17px;font-weight:600;color:#8b9096;width:140px;text-align:center}
.footer{position:absolute;left:0;top:1960px;width:1200px;height:208px;background:var(--footer);color:var(--footer-text)}
.fcol{position:absolute;top:30px;font-size:11px;line-height:1.75}
.fcol h4{color:#fff;font-size:13px;font-weight:600;margin-bottom:8px;display:flex;align-items:center;gap:8px}
.fcol ul{list-style:none}
.fcol li::before{content:"› ";color:var(--footer-text)}
.f1{left:144px}.f2{left:340px}.f3{left:596px}
.fbrand{position:absolute;right:144px;top:34px;text-align:right}
.fbrand .brand-name{color:#fff;font-size:20px}
.fbrand p{font-size:10px;margin-top:10px}
</style>
</head>
<body>
<div class="topline"></div>
<header class="header">
  <div class="contact-strip">
    <span><svg width="11" height="11" viewBox="0 0 24 24"><path fill="#ec1f27" d="M6.6 10.8a15 15 0 0 0 6.6 6.6l2.2-2.2c.3-.3.7-.4 1-.2 1.1.4 2.3.6 3.6.6.6 0 1 .4 1 1V20c0 .6-.4 1-1 1A17 17 0 0 1 3 4c0-.6.4-1 1-1h3.5c.6 0 1 .4 1 1 0 1.3.2 2.5.6 3.6.1.3 0 .7-.2 1z"/></svg>Tel: +1 215 555 0143</span>
    <span><svg width="12" height="10" viewBox="0 0 24 18"><rect x="1" y="1" width="22" height="16" fill="none" stroke="#ec1f27" stroke-width="2"/><path d="M1 1l11 9 11-9" fill="none" stroke="#ec1f27" stroke-width="2"/></svg>E-Mail: hello@halvernservice.com</span>
  </div>
  <div class="brand">
    <div class="brand-dot"></div>
    <div class="brand-name">Halvern<br>Service</div>
  </div>
  <nav class="nav">
    <a class="active" href="#">Home</a>
    <a href="#">About Us</a>
    <a href="#">Products</a>
    <a href="#">Service</a>
    <a href="#">Contact</a>
  </nav>
</header>

<section class="hero">
  <div class="hero-photo" role="img" aria-label="Rooftop air conditioning units under a cloudy sky"></div>
  <form class="booking">
    <h2>Book Your Appoinment</h2>
    <div class="field-row"><div class="field">First Name</div><div class="field">Last Name</div></div>
    <div class="field-row"><div class="field">Phone Number</div><div class="field">Email Address</div></div>
    <div class="field-row"><div class="field">Street Address</div></div>
    <div class="field-row"><div class="field">City</div><div class="field">State</div><div class="field">Zip Code</div></div>
    <div class="field-row"><div class="field">Describe the service you need</div></div>
    <p class="note">* All fields are required to book</p>
    <div class="submit">Submit</div>
  </form>
</section>

<section class="offer">
  <h2 class="section-title">What We Offer</h2>
  <div class="offer-grid">
    <div class="tile"><div class="tile-photo p1" role="img" aria-label="Technician repairing an outdoor unit"></div><div class="tile-label">Repair</div></div>
    <div class="tile"><div class="tile-photo p2" role="img" aria-label="Ceiling air vent being replaced"></div><div class="tile-label">Replacement</div></div>
    <div class="tile"><div class="tile-photo p3" role="img" aria-label="Technician performing maintenance"></div><div class="tile-label">Maintenance</div></div>
    <div class="tile short"><div class="tile-photo p4" role="img" aria-label="New heating system installation"></div><div class="tile-label">New Installations</div></div>
    <div class="tile short"><div class="tile-photo p5" role="img" aria-label="Ductwork in a basement"></div><div class="tile-label">Lorem ipsum dolor sit amet</div></div>
    <div class="tile short"><div class="tile-photo p6" role="img" aria-label="Outdoor condenser beside a house"></div><div class="tile-label">Lorem ipsum dolor sit amet</div></div>
  </div>
  <div class="more-btn">Parcourir tous les produits</div>
</section>

<section class="about-row">
  <div class="about">
    <h3>About Us</h3>
    <div class="about-body">
      <div class="about-photo" role="img" aria-label="Service team in hard hats"></div>
      <p class="about-text">Lorem ipsum dolor sit amet, conse ctetur adipiscing elit. Sed ac congue tellus, tempor volutpat nunc. Duis sit amet commodo ante. Nulla facilisi. Nullam sit amet ex lacus, non pulvinar quam. <a href="#">Read More</a></p>
    </div>
  </div>
  <div class="newsletter">
    <h3>Newsletter Sign Up</h3>
    <p>Stay up to date with seasonal tips, service reminders and special offers. Enter your email below and we will keep you posted every month.</p>
    <div class="sub-row"><div class="sub-field">Email Address</div><div class="sub-btn">Subscribe</div></div>
  </div>
</section>

<section class="award">
  <div class="award-text">
    <h2>we are an harlow's guide top trade<br>award winner</h2>
    <p>Lorem ipsum dolor sit amet, consectetur adipiscing elit. Fusce feugiat tellus nisl,<br>vitae gravida augue aliquam nec.</p>
  </div>
  <div class="award-badge" role="img" aria-label="Award badge"><span></span></div>
</section>

<section class="partners">
  <div class="partner-row r1">
    <div class="partner">Norvale</div><div class="partner">Pembrik</div><div class="partner">Quintrel</div><div class="partner">Solvana</div><div class="partner">Corlith</div>
  </div>
  <div class="partner-row r2">
    <div class="partner">Greenvale</div><div class="partner">Tessaly</div><div class="partner">Velmoor</div><div class="partner">Ardent Air</div><div class="partner">Brightfen</div>
  </div>
</section>

<footer class="footer">
  <div class="fcol f1">
    <h4>Navigation</h4>
    <ul><li>Home</li><li>About Us</li><li>Products</li><li>Service</li><li>Contact</li></ul>
  </div>
  <div class="fcol f2">
    <h4>Liens utiles</h4>
    <ul><li>Terms of Service</li><li>Privacy Policy</li><li>Financing</li><li>Site Map</li></ul>
  </div>
  <div class="fcol f3">
    <h4>Contact us</h4>
    <p>1420 Linden Road, Suite 4<br>Doylestown, PA 18901<br>Tel: +1 215 555 0143<br>hello@halvernservice.com</p>
  </div>
  <div class="fbrand">
    <div class="brand-name">Halvern<br>Service</div>
    <p>© 2024 Halvern Service. All Rights Reserved</p>
  </div>
</footer>
</body>
</html>
```